Artist needs a CD Cover Design (Post-Apocalyptic Ambience)

We need a CD Cover Design, for an Album coming out in june.
The songs on the album are the original soundtrack of a Dance Show, that tells the story of a post-apocalyptic world. The whole plot is driven by a Lantern, that contaminated the world and should be healed later on. Main places are "Glow Harbor", a kind of Las Vegas, "Ashmere Fold" which is a kind of cemetary, "Quarlbury", ruled by the Oil business, "Mollvane" which is a big mine, and the "Hollowmere" where some humans are protected from the pandemy. The main character is a lonely mute young woman.
So, the name of the Album is "Lantern"!
The name should be written on the Cover, in a certain way up to the artist. The color scheme should be more in darkness than joy, as you could figure it out with the story. It would be great if the design could be greater than just the CD cover, in order to be as well on the other side of the CD cover (page 2, 3 and/or 4 of the digipack)
Requirements
Must have
- The name "Lantern" in the design
- A dark-poetic ambience
Nice to have
- A bigger than one-page design (for other sides of the digipack)

```html
<!DOCTYPE html>
<html lang="en">
<head>
<meta charset="utf-8">
<title>Lantern — Ambroise Valet</title>
<link rel="stylesheet" href="https://fonts.googleapis.com/css2?family=Anton&family=Monsieur+La+Doulaise&display=swap">
<style>
  :root {
    --sky-light: #d9d9d9;
    --sky-mid: #9a9a9a;
    --ground-dark: #2b2d2e;
    --ground-deep: #1c1e1f;
    --citadel-gold: #f3d23a;
    --citadel-pale: #ece6ea;
    --title-ink: #050505;
    --artist-gold: #f2d43e;
  }
  html, body {
    margin: 0;
    padding: 0;
    overflow: hidden;
    background: var(--ground-deep);
  }
  .cover {
    position: relative;
    width: 1200px;
    height: 1200px;
    overflow: hidden;
  }
  .cover-artwork {
    position: absolute;
    inset: 0;
    background:
      radial-gradient(ellipse 55% 35% at 50% 38%, rgba(236, 230, 234, 0.85), rgba(243, 210, 58, 0.18) 60%, transparent 80%),
      linear-gradient(180deg, var(--sky-light) 0%, var(--sky-mid) 38%, var(--ground-dark) 66%, var(--ground-deep) 100%);
  }
  .album-title {
    position: absolute;
    left: 0;
    top: 0;
    width: 1200px;
    height: 1200px;
  }
  .album-title text {
    font-family: "Anton", "Impact", sans-serif;
    fill: var(--title-ink);
  }
  .artist-name {
    position: absolute;
    left: 30px;
    bottom: 4px;
    margin: 0;
    font-family: "Monsieur La Doulaise", cursive;
    font-size: 104px;
    line-height: 1;
    font-weight: 400;
    color: var(--artist-gold);
    letter-spacing: 4px;
  }
</style>
</head>
<body>
  <main class="cover">
    <div class="cover-artwork" role="img" aria-label="Stormy grey sky with lightning over a pale gothic citadel of spires edged in gold, overlaid with a halftone dot pattern, above a dark rocky ground"></div>
    <svg class="album-title" viewBox="0 0 1200 1200" aria-label="Lantern">
      <text x="24" y="1125" font-size="470" textLength="1136" lengthAdjust="spacingAndGlyphs">LANTERN</text>
    </svg>
    <h1 class="artist-name">Ambroise Valet</h1>
  </main>
</body>
</html>
```